Fox Hollow Brewing Company Spring 2024

https://www.foxhollowhub.com/
www.FoxhollowBrewing.com
Spring Menu change for Brewery, focus on menu that is upmarket yet fresh and fun. 11"x18" layout both sides. out brand kit online offers a lot of direction with fonts, colors, and logos. We do two menu changes a year and want to keep that same look once we find a great design.
Target Market(s)
30-60 year old
Industry/Entity Type
Brewery Restaurant
Font styles to use
Other font styles liked:
- See Brand Kit
Colors
00AB8E
00BBA5
67D7C9
C6EFE9
E9F9F6
Requirements
Must have
- Menu engineering
Nice to have
- Stock food photos

```html
<!DOCTYPE html>
<html lang="en">
<head>
<meta charset="utf-8">
<title>Fox Hollow Spring 2024 Menu</title>
<link href="https://fonts.googleapis.com/css2?family=Alegreya:ital,wght@0,700;0,900;1,400&family=Kaushan+Script&family=Red+Hat+Display:wght@500;700;800&display=swap" rel="stylesheet">
<style>
:root{
  --backdrop:#48484a;
  --paper:#e9f9f6;
  --mist:#c6eff9;
  --mint:#c6efe9;
  --aqua:#67d7c9;
  --teal:#00bba5;
  --jade:#00ab8e;
  --deep:#0a4f46;
  --accent:#00876f;
  --ink:#1d2b29;
}
*{margin:0;padding:0;box-sizing:border-box}
html,body{width:854px;height:1200px;overflow:hidden;background:var(--backdrop)}
.canvas{position:relative;width:854px;height:1200px}
.sheet{position:absolute;left:96px;top:58px;width:662px;height:1083px;background:var(--paper);box-shadow:6px 8px 14px rgba(0,0,0,.35)}
.masthead{position:absolute;left:96px;top:58px;width:662px;height:188px;background:var(--deep)}
.brand-mark{position:absolute;left:219px;top:122px;width:76px;height:76px;border-radius:50%;background:var(--aqua)}
.brand-name{position:absolute;left:330px;top:128px;font:800 50px/1 "Red Hat Display",sans-serif;color:var(--paper);letter-spacing:2px}
.address{position:absolute;left:330px;top:182px;font:italic 400 19px/1 "Alegreya",serif;color:var(--mint);letter-spacing:1px}
.title{position:absolute;left:136px;top:262px;font:900 47px/1 "Alegreya",serif;color:var(--deep);letter-spacing:-1px}
.subtitle{position:absolute;left:244px;top:322px;font:400 34px/1.2 "Kaushan Script",cursive;color:var(--jade)}
.rule{position:absolute;height:0;border-top:1px solid var(--deep)}
.vrule{position:absolute;width:0;border-left:1px solid var(--deep)}
.dots{position:absolute;height:0;border-top:1px dotted #4d5f5c}
.banner{position:absolute;height:27px}
.banner svg{position:absolute;inset:0}
.banner span{position:relative;display:block;text-align:center;font:700 17px/27px "Alegreya",serif;color:var(--paper)}
.label{position:absolute;font:500 8.5px/1 "Red Hat Display",sans-serif;letter-spacing:1.6px;color:var(--ink)}
.item{position:absolute}
.item .row{display:flex;justify-content:space-between;align-items:baseline;white-space:nowrap}
.item h3{font:700 10.5px/12px "Red Hat Display",sans-serif;letter-spacing:.5px;color:var(--accent)}
.item h3 small{font-size:5.5px;color:var(--deep);letter-spacing:0}
.price{font:800 10.5px/12px "Red Hat Display",sans-serif;color:var(--deep)}
.price sup{font-size:5.5px}
.item p{margin-top:4px;font:500 6.8px/9.3px "Red Hat Display",sans-serif;color:var(--ink)}
.dips{position:absolute;left:336px;top:451px;width:158px;list-style:none}
.dips li{display:flex;justify-content:space-between;font:700 7.8px/14px "Red Hat Display",sans-serif;color:var(--deep);letter-spacing:.4px}
.dips li b{color:var(--jade);margin-right:2px}
.dips li em{font-style:normal;color:var(--jade);font-weight:500}
.dips li.wrap{line-height:9px;margin-top:2px}
.dips li span:last-child{align-self:flex-end}
.box{position:absolute;border:1px solid var(--deep);border-radius:9px;padding:4px}
.box .inner{height:100%;border:1px dotted #4d5f5c;border-radius:6px;text-align:center}
.box h4{font:700 10px/1 "Red Hat Display",sans-serif;color:var(--accent);letter-spacing:.6px}
.box p{font:500 6.8px/9.3px "Red Hat Display",sans-serif;color:var(--ink)}
.box .deal{font:800 9.3px/13.5px "Red Hat Display",sans-serif;color:var(--deep);letter-spacing:.3px}
.addons{display:grid;grid-template-columns:1fr 1fr;column-gap:10px;text-align:left;list-style:none;margin-top:6px}
.addons li{display:flex;justify-content:space-between;font:700 5.6px/9.5px "Red Hat Display",sans-serif;color:var(--deep);letter-spacing:.3px}
.addons li::before{content:"•";margin-right:4px}
.addons li span:first-child{flex:1}
.note{position:absolute;left:544px;top:313px;width:178px;text-align:center;font:italic 400 5.8px/7px "Alegreya",serif;color:var(--accent)}
</style>
</head>
<body>
<div class="canvas">
  <div class="sheet"></div>
  <header class="masthead"></header>
  <div class="brand-mark"></div>
  <div class="brand-name">FOX HOLLOW</div>
  <div class="address">418 Cedar Lane Marble Ridge, Tx 78000</div>

  <h1 class="title">Fox Hollow Spring</h1>
  <div class="subtitle">2024 Menu</div>

  <div class="rule" style="left:129px;top:397px;width:116px"></div>
  <div class="rule" style="left:380px;top:397px;width:116px"></div>
  <div class="banner" style="left:250px;top:384px;width:127px">
    <svg viewBox="0 0 127 27" preserveAspectRatio="none"><polygon points="4,0 127,0 122,13.5 127,27 0,27 5,13.5" fill="var(--deep)"/></svg>
    <span>Appetizers</span>
  </div>

  <div class="label" style="left:131px;top:429px">CHIPS AND ...</div>
  <div class="label" style="left:269px;top:429px">(HALF/FULL)</div>

  <div class="vrule" style="left:313px;top:450px;height:449px"></div>
  <div class="vrule" style="left:523px;top:272px;height:843px"></div>

  <div class="item" style="left:131px;top:455px;width:151px">
    <div class="row"><h3>THE TRIO</h3><span class="price">$14</span></div>
    <p>A half-size serving each of the Fox Hollow Blonde Beer Cheese, Guacamole, and Salsa.</p>
  </div>
  <div class="dots" style="left:130px;top:516px;width:155px"></div>
  <div class="item" style="left:131px;top:532px;width:151px">
    <div class="row"><h3>GRIZZLY QUESO</h3><span class="price">7 / 11.5</span></div>
    <p>Fox Hollow Blonde Beer Cheese topped with guac, pico de gallo, and cotija cheese.</p>
  </div>
  <div class="dots" style="left:130px;top:589px;width:155px"></div>
  <div class="item" style="left:131px;top:606px;width:151px">
    <div class="row"><h3>TRUFFLE SPROUTS <small>(V)</small></h3><span class="price">$11<sup>5</sup></span></div>
    <p>Fresh fried Brussels sprouts topped with truffle aioli, pecans, and Asiago cheese.</p>
  </div>
  <div class="dots" style="left:130px;top:663px;width:155px"></div>
  <div class="item" style="left:131px;top:680px;width:151px">
    <div class="row"><h3>TEXAS POUTINE</h3><span class="price">$10</span></div>
    <p>French fries topped with ancho cheddar gravy, chopped brisket, pico de gallo.</p>
  </div>
  <div class="dots" style="left:130px;top:740px;width:155px"></div>
  <div class="item" style="left:131px;top:760px;width:151px">
    <div class="row"><h3>CHEESE CURDS</h3><span class="price">$9<sup>5</sup></span></div>
    <p>Crispy fried cheesy goodness. Served with a zesty chipotle-lime sauce.</p>
  </div>
  <div class="dots" style="left:130px;top:817px;width:155px"></div>
  <div class="item" style="left:131px;top:836px;width:152px">
    <div class="row"><h3 style="letter-spacing:.3px">EMBELLISHED NACHOS</h3><span class="price">$11<sup>5</sup></span></div>
    <p style="margin-top:1px;line-height:7.6px">Corn tortilla chips with Fox Hollow Blonde Beer Cheese, red sauce, Cotija cheese, lettuce, pico de gallo, pickled onions, jalapeños, and sour cream.</p>
  </div>

  <ul class="dips">
    <li><span><b>•</b>GUACAMOLE <em>(V)</em></span><span>6.5 / 11</span></li>
    <li><span><b>•</b>SALSA <em>(V)</em></span><span>6 / 9.5</span></li>
    <li class="wrap"><span><b>•</b>FOX HOLLOW BLONDE BEER<br>&nbsp;&nbsp;CHEESE:</span><span>6.5 / 11.5</span></li>
  </ul>
  <div class="dots" style="left:338px;top:516px;width:156px"></div>
  <div class="item" style="left:339px;top:532px;width:150px">
    <div class="row"><h3>TRUFFLE FRIES <small>(V)</small></h3><span class="price">$8</span></div>
    <p>Truffle salted french fries. Served with truffle aioli, garnished with shredded Asiago.</p>
  </div>
  <div class="dots" style="left:338px;top:589px;width:156px"></div>
  <div class="item" style="left:339px;top:606px;width:150px">
    <div class="row"><h3>ONION RINGS</h3><span class="price">$8<sup>5</sup></span></div>
    <p>Beer battered onion rings served with house-made Hollow sauce.</p>
  </div>
  <div class="dots" style="left:322px;top:663px;width:157px"></div>

  <div class="box" style="left:334px;top:681px;width:160px;height:112px">
    <div class="inner" style="padding-top:16px">
      <h4>CHICKEN WINGS:</h4>
      <p style="margin:6px 10px 0">Chicken wings hand tossed in your choice of sauce. Served with celery and ranch or blue cheese.</p>
      <p class="deal" style="margin:6px 8px 0">6 FOR $10.5, 12 FOR $16, 18 FOR $22</p>
    </div>
  </div>
  <div class="box" style="left:334px;top:811px;width:160px;height:66px">
    <div class="inner" style="padding:14px 8px 0">
      <h4>ADD-ONS</h4>
      <ul class="addons">
        <li><span>BRISKET</span><span>$4</span></li>
        <li><span>ASADA</span><span>$3</span></li>
        <li><span>PORK BELLY</span><span>$3</span></li>
        <li><span>CHICKEN</span><span>$3</span></li>
      </ul>
    </div>
  </div>

  <div class="rule" style="left:129px;top:927px;width:116px"></div>
  <div class="rule" style="left:380px;top:927px;width:116px"></div>
  <div class="banner" style="left:250px;top:914px;width:127px">
    <svg viewBox="0 0 127 27" preserveAspectRatio="none"><polygon points="4,0 127,0 122,13.5 127,27 0,27 5,13.5" fill="var(--deep)"/></svg>
    <span>Salads</span>
  </div>
  <div class="label" style="left:269px;top:952px">(HALF/FULL)</div>
  <div class="vrule" style="left:313px;top:973px;height:142px"></div>

  <div class="item" style="left:132px;top:977px;width:147px">
    <div class="row"><h3>WEDGE SALAD</h3><span class="price">6 / 11</span></div>
    <p>Iceberg lettuce with bacon crumbles, tomatoes, blue cheese crumbles, and blue cheese dressing.</p>
  </div>
  <div class="item" style="left:327px;top:977px;width:167px">
    <div class="row"><h3>THE SEASONAL ONE <small>(GF) (V)</small></h3><span class="price">6 / 11</span></div>
    <p>Truffle salted french fries. Served with truffle aioli, garnished with shredded Asiago.</p>
  </div>
  <div class="dots" style="left:130px;top:1039px;width:155px"></div>
  <div class="dots" style="left:327px;top:1039px;width:167px"></div>
  <div class="item" style="left:132px;top:1059px;width:147px">
    <div class="row"><h3>THE CHAMP <small>(V)</small></h3><span class="price">6 / 11</span></div>
    <p>Spring mix with tomato, avocado, cucumber, and red onion. Served with jalapeño-cilantro dressing and topped with crisp tortilla strips.</p>
  </div>
  <div class="item" style="left:327px;top:1059px;width:167px">
    <div class="row"><h3>EL OSO <small>(GF) (V)</small></h3><span class="price">6 / 11</span></div>
    <p>Romaine lettuce with grilled corn, black beans, tomatoes, red onion, bell peppers, and chipotle-lime dressing. Topped with Cotija cheese.</p>
  </div>

  <div class="banner" style="left:568px;top:279px;width:125px">
    <svg viewBox="0 0 125 27" preserveAspectRatio="none"><polygon points="4,0 125,0 120,13.5 125,27 0,27 5,13.5" fill="var(--deep)"/></svg>
    <span>Burgers</span>
  </div>
  <div class="note">All half-pound burgers are cooked medium-well and served on a toasted butter brioche bun with a side of fries, lettuce, tomato, onion and home-made pickles.</div>

  <div class="dots" style="left:548px;top:348px;width:170px"></div>
  <div class="item" style="left:549px;top:360px;width:168px">
    <div class="row"><h3>THE CLASSIC ONE <small>(V)</small></h3><span class="price">$12<sup>5</sup></span></div>
    <p style="width:140px">8 oz. Oak Ridge Farms patty with lettuce, tomato, onion, and home-made pickles.</p>
  </div>
  <div class="dots" style="left:548px;top:413px;width:170px"></div>
  <div class="item" style="left:549px;top:428px;width:168px">
    <div class="row"><h3>EGGSILLENT GUY</h3><span class="price">$15<sup>25</sup></span></div>
    <p style="width:150px">Breakfast burger with bacon, cheddar, a fried egg, and Hollow sauce.</p>
  </div>
  <div class="dots" style="left:548px;top:482px;width:170px"></div>
  <div class="item" style="left:549px;top:499px;width:168px">
    <div class="row"><h3>THE FARMER’S CUT</h3><span class="price">$14<sup>75</sup></span></div>
    <p style="width:156px">8 oz. Oak Ridge Farms patty with jack cheese, thick cut bacon, grilled mushrooms, and white truffle aioli.</p>
  </div>
  <div class="dots" style="left:548px;top:561px;width:170px"></div>
  <div class="item" style="left:549px;top:576px;width:168px">
    <div class="row"><h3>THE LEGENDARY ONE</h3><span class="price">$14<sup>75</sup></span></div>
    <p style="width:156px">8 oz. Oak Ridge Farms patty with thick cut bacon, caramelized onions, aged cheddar, and roasted garlic aioli.</p>
  </div>
  <div class="dots" style="left:548px;top:642px;width:170px"></div>
  <div class="item" style="left:549px;top:656px;width:168px">
    <div class="row"><h3>THE LAREDO ONE</h3><span class="price">$15<sup>5</sup></span></div>
    <p style="width:156px">Jack Cheese, Pico de gallo, Mashed avocado, pickled jalapenos with chipotle aioli.</p>
  </div>
  <div class="dots" style="left:548px;top:710px;width:170px"></div>
  <div class="item" style="left:549px;top:724px;width:168px">
    <div class="row"><h3>THE LUBBOCK</h3><span class="price">$15<sup>5</sup></span></div>
    <p style="width:140px">Bacon, Cheddar cheese, onion rings, BBQ sauce.</p>
  </div>
  <div class="dots" style="left:548px;top:776px;width:170px"></div>
  <div class="item" style="left:550px;top:797px;width:167px">
    <div class="row"><h3>EL DORADO</h3><span class="price">$16</span></div>
    <p style="width:150px">Half-pound burger with pork belly, cheddar cheese, and horseradish mustard aioli.</p>
  </div>
  <div class="dots" style="left:548px;top:857px;width:170px"></div>
  <div class="item" style="left:549px;top:874px;width:168px">
    <div class="row"><h3>ROYALE WITH CHEESE</h3><span class="price">$14<sup>5</sup></span></div>
    <p style="width:158px">Served on Texas toast with caramelized onions, cheddar cheese, and Monterey Jack Cheese with Hollow sauce.</p>
  </div>
  <div class="dots" style="left:548px;top:935px;width:170px"></div>

  <div class="box" style="left:547px;top:951px;width:168px;height:68px">
    <div class="inner" style="padding:13px 10px 0">
      <h4>ADD-ONS</h4>
      <ul class="addons" style="margin-top:8px">
        <li><span>CHEESE</span><span>$1</span></li>
        <li><span>BACON</span><span>$2</span></li>
        <li><span>JALAPEÑOS</span><span>$1</span></li>
        <li style="line-height:7px"><span>CARAMELIZED<br>ONIONS</span><span style="align-self:flex-end">$1</span></li>
      </ul>
    </div>
  </div>
  <div class="box" style="left:547px;top:1037px;width:168px;height:68px">
    <div class="inner" style="padding:14px 14px 0">
      <h4>ADD-ONS</h4>
      <ul class="addons" style="grid-template-columns:1fr;margin-top:7px;row-gap:2px">
        <li><span>PICK ANY OF OUR SALADS</span><span>$2</span></li>
        <li><span>TRUFFLE FRIES</span><span>$2</span></li>
      </ul>
    </div>
  </div>
</div>
</body>
</html>
```